Business Card Design Project - Brindle Media

We need a new business card that fits with our new logo. We are a social media agency and consultancy operating in China. We want a fresh and strong business card. Our cards need to be two-sided as we have both English and Chinese language names and addresses on the card, but as with our current business card this does not need to be a mirror-image. Our thoughts go out to a white card on the front where the logo/name is and then using the logo colours for different coloured back-grounds. i.e that the back of the biz card works with the four different colours in the logo.

Attached is the new logo, and also a copy of our old business cards.

Target Market(s)

CEO's, CMO's. media and advertising professionals

Industry/Entity Type

Business

Requirements
Must have
• inclusion of both Chinese and English language
Nice to have
• four different colored versions of the back of the biz card. Our logo has four colors and each of these colors we would like to have a version of.

```html
<!DOCTYPE html>
<html lang="en">
<head>
<meta charset="utf-8">
<title>Brindle Media – Business Cards</title>
<link rel="stylesheet" href="https://fonts.googleapis.com/css2?family=Arimo:wght@400;700&family=Noto+Sans+SC:wght@400&family=Open+Sans:wght@400;600&display=swap">
<style>
  :root {
    --stage: #2b2b2b;
    --green: #7dc421;
    --purple: #6e1a8c;
    --orange: #e8581e;
    --pink: #e2087f;
    --paper: #f3f3f3;
    --bar: #ececec;
    --ink: #111111;
    --grey-text: #555555;
    --on-colour: #f4f4ec;
  }
  * { box-sizing: border-box; margin: 0; padding: 0; }
  html, body { width: 1200px; height: 900px; overflow: hidden; }
  body { background: var(--stage); position: relative; font-family: "Open Sans", sans-serif; }

  .card {
    position: absolute;
    width: 600px;
    height: 360px;
    transform-origin: top left;
    overflow: hidden;
  }
  .card--small { transform: scale(0.5); }

  .card--green  { --accent: var(--green); }
  .card--purple { --accent: var(--purple); }
  .card--orange { --accent: var(--orange); }
  .card--pink   { --accent: var(--pink); }

  /* Back side: coloured */
  .card--back { background: var(--accent); color: var(--on-colour); }
  .card--back .side-bar { position: absolute; width: 28px; background: var(--bar); }
  .card--back .side-bar--left { left: 0; top: 0; height: 205px; }
  .card--back .side-bar--right { right: 0; top: 205px; height: 155px; }
  .card--back .wordmark {
    position: absolute; right: 28px; top: 22px;
    font-size: 58px; font-weight: 600; line-height: 0.95;
    text-align: right; color: var(--on-colour); letter-spacing: -1px;
  }
  .card--back .address { position: absolute; left: 132px; top: 200px; }
  .address .address-cn { font-family: "Noto Sans SC", sans-serif; font-size: 13px; line-height: 19px; }
  .address .address-en { font-size: 16px; line-height: 25px; margin-top: 8px; }
  .address .contact { font-size: 16px; margin-top: 16px; }

  /* Front side: white */
  .card--front { background: var(--paper); color: var(--ink); }
  .card--front .accent-block { position: absolute; top: 68px; width: 29px; height: 52px; background: var(--accent); }
  .card--front .accent-block--left { left: 0; }
  .card--front .accent-block--right { right: 0; }
  .card--front .web-line {
    position: absolute; top: 88px; left: 0; width: 100%;
    text-align: center; font-size: 16px; color: var(--grey-text); letter-spacing: 0.3px;
  }
  .card--front .person { position: absolute; right: 337px; top: 205px; text-align: right; font-family: "Arimo", sans-serif; }
  .person .person-name { font-size: 22px; font-weight: 700; letter-spacing: 0.5px; }
  .person .person-role { font-size: 14px; margin-top: 4px; }
  .card--front .wordmark {
    position: absolute; left: 312px; top: 196px;
    font-size: 40px; font-weight: 600; line-height: 0.95;
    color: var(--ink); letter-spacing: -1px;
  }
</style>
</head>
<body>

  <!-- Large back, green -->
  <section class="card card--back card--green" style="left:68px; top:46px;">
    <div class="side-bar side-bar--left"></div>
    <div class="side-bar side-bar--right"></div>
    <div class="wordmark">Brindle<br>Media</div>
    <div class="address">
      <p class="address-cn">北京市朝阳区兰亭商务中心</p>
      <p class="address-cn">枫南路兰亭商务中心C310室（100000）</p>
      <p class="address-en">Suite C310, Lantern Court Business Centre<br>Maple South Rd Harbour District, Beijing 100000</p>
      <p class="contact">Phone: +86 13800451272 | skype: owenbeijing</p>
    </div>
  </section>

  <!-- Large front, white -->
  <section class="card card--front card--green" style="left:72px; top:492px;">
    <div class="accent-block accent-block--left"></div>
    <div class="accent-block accent-block--right"></div>
    <p class="web-line">owen@hartleymail.com | www.brindlechina.com</p>
    <div class="person">
      <p class="person-name">Owen Hartley</p>
      <p class="person-role">managing director</p>
    </div>
    <div class="wordmark">Brindle<br>Media</div>
  </section>

  <!-- Colour backs -->
  <section class="card card--back card--purple card--small" style="left:848px; top:58px;">
    <div class="side-bar side-bar--left"></div>
    <div class="side-bar side-bar--right"></div>
    <div class="wordmark">Brindle<br>Media</div>
    <div class="address">
      <p class="address-cn">北京市朝阳区兰亭商务中心</p>
      <p class="address-cn">枫南路兰亭商务中心C310室（100000）</p>
      <p class="address-en">Suite C310, Lantern Court Business Centre<br>Maple South Rd Harbour District, Beijing 100000</p>
      <p class="contact">Phone: +86 13800451272 | skype: owenbeijing</p>
    </div>
  </section>

  <section class="card card--back card--orange card--small" style="left:735px; top:193px;">
    <div class="side-bar side-bar--left"></div>
    <div class="side-bar side-bar--right"></div>
    <div class="wordmark">Brindle<br>Media</div>
    <div class="address">
      <p class="address-cn">北京市朝阳区兰亭商务中心</p>
      <p class="address-cn">枫南路兰亭商务中心C310室（100000）</p>
      <p class="address-en">Suite C310, Lantern Court Business Centre<br>Maple South Rd Harbour District, Beijing 100000</p>
      <p class="contact">Phone: +86 13800451272 | skype: owenbeijing</p>
    </div>
  </section>

  <section class="card card--back card--pink card--small" style="left:848px; top:285px;">
    <div class="side-bar side-bar--left"></div>
    <div class="side-bar side-bar--right"></div>
    <div class="wordmark">Brindle<br>Media</div>
    <div class="address">
      <p class="address-cn">北京市朝阳区兰亭商务中心</p>
      <p class="address-cn">枫南路兰亭商务中心C310室（100000）</p>
      <p class="address-en">Suite C310, Lantern Court Business Centre<br>Maple South Rd Harbour District, Beijing 100000</p>
      <p class="contact">Phone: +86 13800451272 | skype: owenbeijing</p>
    </div>
  </section>

  <!-- Colour fronts -->
  <section class="card card--front card--purple card--small" style="left:781px; top:525px;">
    <div class="accent-block accent-block--left"></div>
    <div class="accent-block accent-block--right"></div>
    <p class="web-line">owen@hartleymail.com | www.brindlechina.com</p>
    <div class="person">
      <p class="person-name">Owen Hartley</p>
      <p class="person-role">managing director</p>
    </div>
    <div class="wordmark">Brindle<br>Media</div>
  </section>

  <section class="card card--front card--pink card--small" style="left:818px; top:583px;">
    <div class="accent-block accent-block--left"></div>
    <div class="accent-block accent-block--right"></div>
    <p class="web-line">owen@hartleymail.com | www.brindlechina.com</p>
    <div class="person">
      <p class="person-name">Owen Hartley</p>
      <p class="person-role">managing director</p>
    </div>
    <div class="wordmark">Brindle<br>Media</div>
  </section>

  <section class="card card--front card--orange card--small" style="left:849px; top:660px;">
    <div class="accent-block accent-block--left"></div>
    <div class="accent-block accent-block--right"></div>
    <p class="web-line">owen@hartleymail.com | www.brindlechina.com</p>
    <div class="person">
      <p class="person-name">Owen Hartley</p>
      <p class="person-role">managing director</p>
    </div>
    <div class="wordmark">Brindle<br>Media</div>
  </section>

</body>
</html>
```